Advertising agency needs site design

You will be designing a clean (plenty of white space) and vivid (colorful) design that is for an advertising agency named Brightwell Reach. Their current web site is located at www.BrightwellReach.net. From there you can see their services and get a feel for the company as the site stands today.
The following are direct quotes from the client:
“I want a clean look with colors of the teal blue, deep yellow (in logo) and then a good energetic orange (deep orange - rich) should bring a good feel and enthusiasm.”
“The orange can be a nice accent color, not dominant.”
“Saw two other things I like - the website lanternkitestudio.com was pretty cool. I liked how the top banner changed colors as you moved to different tabs. I am somewhat wanting the colors I mentioned - like the blue color we use can be lighter as long as it works with the logo. - love the tulip forge site. I want quirky, creative and clean look - fun feel but slightly sophisticated to work with the medical field.”
Brightwell Reach currently focuses on the following primary industries:
• Medical / Health Care – Currently the primary industry
• Retail Industry
• Automotive Industry
• Entertainment Industry
Primary Services
• Media Planning & Buying: Web, TV, Print, Radio
• Campaign monitoring and reporting
• Commercial Production: TV & Radio
• Strategic Planning
• Market Research
• Internet Marketing: Email, SEO, Web design / development
Primary Navigation will consist of the following:
• Home
• About Us
o History
o Principal Profile (sub nav)
o Sales Team & Partners
• Clients
• Services
• Testimonials
• Contact Us
They want the web site to act as a basis for future marketing collateral so the overall feel from the web site must be capable of translating to print and other collateral. I do not currently have a clean digital version of their logo however their logo is on the web site (brightwellreach.net)
Reason: Still awaiting feedback from client on designs. They should be back to us shortly.
Target Market(s)
larger companies that are purchasing air time on television and radio. Typically in the health care industry and others described above in brief.
Industry/Entity Type
Advertising
Look and feel
Each slider illustrates characteristics of the customer's brand and the style your logo design should communicate.

```html
<!DOCTYPE html>
<html lang="en">
<head>
<meta charset="utf-8">
<title>Brightwell Reach</title>
<link href="https://fonts.googleapis.com/css2?family=Arimo:wght@400;700&display=swap" rel="stylesheet">
<style>
:root{
  --navy:#0b4e7b;
  --navy-dark:#0d2f47;
  --navy-deep:#0a2538;
  --sun:#f8b534;
  --ink:#333;
  --muted:#666;
  --link-blue:#1d6fa5;
  --teal:#1ba6b3;
  --green:#6cae1f;
  --red:#e0480f;
  --purple:#6a3b98;
  --white:#fff;
}
*{margin:0;padding:0;box-sizing:border-box}
html,body{width:963px;height:1200px;overflow:hidden;background:var(--white)}
body{position:relative;font-family:"Arimo",Arial,sans-serif;color:var(--ink)}
h1,h2,h3{font-weight:400}
.abs{position:absolute}

.site-header{left:0;top:0;width:963px;height:103px;background:var(--navy)}
.brand{left:60px;top:30px;display:flex;align-items:center;gap:10px;color:var(--white);font-size:27px;letter-spacing:1px}
.brand-dot{width:12px;height:12px;border-radius:50%;background:var(--sun)}
.account-links{right:52px;top:12px;font-size:11px;color:var(--sun);letter-spacing:.5px}
.account-links span{margin:0 5px;color:var(--white)}
.call-box{left:659px;top:44px;width:218px;height:47px;background:var(--white);border-radius:4px}
.call-agent{left:6px;top:-20px;width:48px;height:64px;border-radius:4px;background:linear-gradient(#e0a070,#333 70%)}
.call-label{left:72px;top:6px;font-size:13px;font-weight:700;color:var(--navy-dark)}
.call-number{left:72px;top:21px;font-size:19px;font-weight:700;color:var(--navy-dark)}

.main-nav{left:0;top:103px;width:963px;height:33px;background:linear-gradient(#fff,#eee);border-bottom:1px solid #ddd}
.main-nav ul{list-style:none;position:absolute;left:48px;top:0;display:flex;height:33px}
.main-nav li{padding:0 18px;line-height:33px;font-size:13px;color:var(--link-blue);border-right:1px solid #ddd}
.main-nav li:last-child{border-right:0}
.search{left:706px;top:106px;width:197px;height:25px;border:1px solid #ccc;background:var(--white);font-size:11px;color:#888;padding:6px 8px}

.sun-band{left:0;top:136px;width:963px;height:259px;background:var(--sun)}
.page{left:44px;top:145px;width:876px;height:817px;background:var(--white)}
.hero{left:50px;top:151px;width:864px;height:280px;background:linear-gradient(90deg,#3a2710,#8a5a1e 45%,#6e4716 75%,#a06a24)}
.hero-dots{left:88px;top:407px;display:flex;gap:8px}
.hero-dots i{width:13px;height:13px;border-radius:50%;background:#ccc}
.hero-dots i:first-child{background:var(--sun)}

.industry-tab{top:449px;height:39px;border-radius:4px;color:var(--white);font-size:16px;padding:9px 12px;overflow:hidden}
.industry-tab svg{position:absolute;right:0;top:0}
.tab-medical{left:53px;width:205px;background:var(--teal)}
.tab-retail{left:270px;width:206px;background:var(--green)}
.tab-auto{left:486px;width:207px;background:var(--red)}
.tab-ent{left:705px;width:205px;background:var(--purple)}

.welcome-title{left:63px;top:508px;font-size:19px;color:var(--muted)}
.welcome-title b{font-weight:400;color:var(--link-blue)}
.welcome-text{left:63px;top:536px;width:569px;font-size:11px;line-height:17.2px;color:var(--muted);text-align:justify;letter-spacing:.95px}
.services-title{left:659px;top:508px;font-size:17px;color:var(--muted)}
.services-list{left:657px;top:537px;width:253px;list-style:none}
.services-list li{height:23px;margin-bottom:3.5px;background:#ececec;font-size:12px;color:var(--muted);line-height:23px;padding-left:28px;position:relative;letter-spacing:.3px}
.services-list li::before{content:"";position:absolute;left:9px;top:8px;border-left:5px solid var(--link-blue);border-top:4px solid transparent;border-bottom:4px solid transparent}

.bottom-band{left:44px;top:718px;width:876px;height:244px;background:var(--sun);border-radius:0 0 8px 8px}
.band-title{top:724px;font-size:17px;color:var(--navy-dark)}
.news-item{left:55px;width:225px;border-bottom:1px dashed var(--white);padding-bottom:4px}
.news-date{font-size:11px;font-weight:700;color:var(--white);letter-spacing:.5px}
.news-text{font-size:11px;color:var(--white);line-height:15px;margin-top:6px}
.read-more{left:198px;top:940px;font-size:10px;font-weight:700;color:var(--navy-dark)}
.quote{left:360px;top:749px;width:218px;height:134px;background:var(--white);border-radius:16px;padding:18px 18px 0 24px;font-size:11px;line-height:14.5px;color:var(--muted)}
.quote-mark{left:373px;top:768px;font-size:22px;color:#555;font-family:Georgia,serif}
.quote-tail{left:375px;top:880px}
.pager{font-size:11px;font-weight:700;color:var(--navy-dark)}
.author{left:380px;top:907px;font-size:11px;color:var(--muted)}
.author b{font-style:italic;color:var(--navy)}
.author-mail{left:380px;top:927px;font-size:11px;color:var(--muted)}
.newsletter-note{left:690px;top:756px;font-size:11px;color:var(--white)}
.newsletter-input{left:687px;top:775px;width:221px;height:27px;background:var(--white);border-radius:4px;font-size:11px;color:#999;padding:7px 10px}
.submit{left:822px;top:809px;width:85px;height:26px;background:#3a3a3a;border-radius:4px;color:var(--white);font-size:13px;font-weight:700;text-align:center;line-height:26px;letter-spacing:1px}
.client-box{left:700px;top:865px;width:194px;height:72px;background:var(--white);border-radius:8px;text-align:center;font-size:17px;font-weight:700;color:#333;line-height:24px;padding-top:12px;letter-spacing:1px}

.site-footer{left:0;top:962px;width:963px;height:238px;background:var(--navy-dark)}
.footer-col{top:978px;color:var(--white)}
.footer-col h4{font-size:12px;font-weight:700;letter-spacing:1px;margin-bottom:14px}
.footer-col ul{list-style:none;font-size:11px;letter-spacing:.5px}
.footer-col li{height:21px;position:relative;padding-left:14px}
.footer-col li::before{content:"";position:absolute;left:0;top:5px;width:4px;height:4px;background:var(--white);border-radius:50%}
.social-sq{position:absolute;left:100px;top:0;width:12px;height:12px;border-radius:2px}
.contact-lines{font-size:11px;line-height:19px;letter-spacing:.3px}
.contact-row{display:flex;align-items:center;gap:10px;margin-top:6px;font-size:11px}
.copyright{left:0;top:1152px;width:963px;height:48px;background:var(--navy-deep);color:#cfd8e0;font-size:11px;text-align:center;line-height:46px;letter-spacing:.5px}
</style>
</head>
<body>

<header class="abs site-header">
  <div class="abs brand"><span class="brand-dot"></span>brightwell reach</div>
  <div class="abs account-links">LOGIN<span>|</span>SIGN UP</div>
  <div class="abs call-box">
    <div class="abs call-agent" role="img" aria-label="Illustration of a support agent with headset"></div>
    <div class="abs call-label">CALL US</div>
    <div class="abs call-number">123 555 0147</div>
  </div>
</header>

<nav class="abs main-nav">
  <ul>
    <li>Home</li><li>About Us</li><li>Clients</li><li>Services</li><li>Testimonials</li><li>Contact Us</li>
  </ul>
</nav>
<div class="abs search">Search
  <svg class="abs" style="right:6px;top:5px" width="14" height="14" viewBox="0 0 14 14"><circle cx="6" cy="6" r="4.2" fill="none" stroke="#1d6fa5" stroke-width="2"/><line x1="9" y1="9" x2="13" y2="13" stroke="#1d6fa5" stroke-width="2.2"/></svg>
</div>

<div class="abs sun-band"></div>
<div class="abs page"></div>

<div class="abs hero" role="img" aria-label="Banner photo of a smiling man in a suit with handwritten service words: Automotive, Strategic Planning, Medical, Retail, Web design, Internet Marketing, Entertainment"></div>
<div class="abs hero-dots"><i></i><i></i><i></i><i></i></div>

<div class="abs industry-tab tab-medical">Medical / Health
  <svg width="40" height="39" viewBox="0 0 40 39"><path d="M8 39 C14 30 14 6 26 4" fill="none" stroke="#fff" stroke-width="1.6"/><path d="M26 30h6M29 27v6" stroke="#fff" stroke-width="1.4"/></svg></div>
<div class="abs industry-tab tab-retail">Retail
  <svg width="40" height="39" viewBox="0 0 40 39"><path d="M8 39 C14 30 14 6 26 4" fill="none" stroke="#fff" stroke-width="1.6"/><path d="M26 30h6M29 27v6" stroke="#fff" stroke-width="1.4"/></svg></div>
<div class="abs industry-tab tab-auto">Automotive
  <svg width="40" height="39" viewBox="0 0 40 39"><path d="M8 39 C14 30 14 6 26 4" fill="none" stroke="#fff" stroke-width="1.6"/><path d="M26 30h6M29 27v6" stroke="#fff" stroke-width="1.4"/></svg></div>
<div class="abs industry-tab tab-ent">Entertainment
  <svg width="40" height="39" viewBox="0 0 40 39"><path d="M8 39 C14 30 14 6 26 4" fill="none" stroke="#fff" stroke-width="1.6"/><path d="M26 30h6M29 27v6" stroke="#fff" stroke-width="1.4"/></svg></div>

<h1 class="abs welcome-title">Welcome to <b>brightwell reach</b></h1>
<p class="abs welcome-text">Lorem ipsum dolor sit amet, consectetuer adipiscing elit. Aenean commodo ligula eget dolor. Aenean massa. Cum sociis natoque penatibus et magnis dis parturient montes, nascetur ridiculus mus. Donec quam felis, ultricies nec, pellentesque eu, pretium quis, sem. Nulla consequat massa quis enim. Donec pede justo, fringilla vel, aliquet nec, vulputate eget, arcu.Lorem ipsum dolor sit amet, consectetuer adipiscing elit. Aenean commodo ligula eget dolor. Aenean massa. Cum sociis natoque gnis dis parturient montes, nascetur ridiculus mus. Donec quam felis, ultricies nec, pellentesque eu, pretium quis, sem. Nulla consequat massa quis enim. Donec pede justo, fringilla vel, aliquet nec, vulputate eget, arcu.n commodo ligula eget dolor. Aenean massa.</p>

<h2 class="abs services-title">Services</h2>
<ul class="abs services-list">
  <li>Media Planning &amp; Buying</li>
  <li>Campaign monitoring and reporting</li>
  <li>Commercial Production</li>
  <li>Strategic Planning</li>
  <li>Market Research</li>
  <li>Internet Marketing</li>
</ul>

<div class="abs bottom-band"></div>

<h3 class="abs band-title" style="left:55px">News</h3>
<div class="abs news-item" style="top:757px"><div class="news-date">MAY 19, 2011</div><div class="news-text">Lorem ipsum dolor sit ametconsectetuer adipiscing elit. Aenean</div></div>
<div class="abs news-item" style="top:822px"><div class="news-date">MAY 19, 2011</div><div class="news-text">Lorem ipsum dolor sit ametconsectetuer adipiscing elit. Aenean</div></div>
<div class="abs news-item" style="top:888px;border-bottom:0"><div class="news-date">MAY 19, 2011</div><div class="news-text">Lorem ipsum dolor sit ametconsectetuer adipiscing elit. Aenean</div></div>
<div class="abs read-more">Read more &gt;&gt;</div>

<h3 class="abs band-title" style="left:360px">Testimonials</h3>
<div class="abs quote">Lorem ipsum dolor sit ametcon-sectetuer adipiscing elit. Aenean commodo ligula eget doloAenean massa. Cum eget doloAenean massa. Cum sociis sociis</div>
<div class="abs quote-mark">&ldquo;</div>
<svg class="abs quote-tail" width="24" height="24" viewBox="0 0 24 24"><path d="M0 0H22L2 22Z" fill="#fff"/></svg>
<div class="abs pager" style="left:542px;top:888px">&lt; &gt;</div>
<div class="abs author"><b>Name</b>, webdesigner</div>
<div class="abs author-mail">oakfieldstudio@mailbox.net</div>

<h3 class="abs band-title" style="left:683px">Newsletter</h3>
<div class="abs newsletter-note">Sign up for our Newsletters</div>
<div class="abs newsletter-input">Enter you email</div>
<div class="abs submit">SUBMIT</div>
<h3 class="abs band-title" style="left:692px;top:840px">Our Clients</h3>
<div class="abs client-box">HERE COMES LOGO<br>CLIENTS</div>
<div class="abs pager" style="left:870px;top:944px">&lt; &gt;</div>

<footer class="abs site-footer"></footer>
<div class="abs footer-col" style="left:56px"><h4>Company</h4>
  <ul><li>Home</li><li>About Us</li><li>Contact Us</li><li>Privacy Policy</li><li>Tearms of use</li></ul></div>
<div class="abs footer-col" style="left:189px"><h4>Industries</h4>
  <ul><li>Medical / Health Care</li><li>Retail</li><li>Automotive</li><li>Entertainment</li></ul></div>
<div class="abs footer-col" style="left:362px"><h4>Services</h4>
  <ul><li>Media Planning &amp; Buying C</li><li>Campaign monitoring and reporting</li><li>Commercial Production</li><li>Strategic Planning</li><li>Market Research</li><li>Internet Marketing</li></ul></div>
<div class="abs footer-col" style="left:601px"><h4>Follow Us</h4>
  <ul>
    <li>Rss<span class="social-sq" style="background:#e8772e"></span></li>
    <li>Chirpline<span class="social-sq" style="background:#6fc6e0"></span></li>
    <li>Friendwall<span class="social-sq" style="background:#3b5c9c"></span></li>
  </ul></div>
<div class="abs footer-col" style="left:738px"><h4>Contact Us</h4>
  <div class="contact-lines">Brightwell Reach, Inc.<br>4820 Harlow Avenue, Suite 310<br>Millbrook, Texas 75990</div>
  <div class="contact-row" style="padding-left:4px">
    <svg width="16" height="12" viewBox="0 0 16 12"><path d="M1 4C5 0 11 0 15 4L13 6 10 4V3H6V4L3 6Z" fill="#fff"/><rect x="4" y="6" width="8" height="5" rx="1" fill="#fff"/></svg>
    &nbsp;555.201.7734&nbsp; (P)</div>
  <div class="contact-row" style="padding-left:4px">
    <svg width="16" height="14" viewBox="0 0 16 14"><rect x="4" y="0" width="8" height="4" fill="#fff"/><rect x="1" y="4" width="14" height="6" rx="1" fill="#fff"/><rect x="4" y="9" width="8" height="5" fill="#fff" stroke="#0d2f47"/></svg>
    &nbsp;555.201.7790&nbsp; (F)</div>
</div>
<div class="abs copyright">2011 &copy; brightwellreach.com. All rights reserved.</div>

</body>
</html>
```